Roving Kneadery Business Cards

Hi Bogdan,
Thank you for designing my awesome logo! It's awesome. Now I need help in designing my business card. The business card is 3.5" x 2.0". I tried downloading my logo to PressLoom to make my business cards but the design would not fit to scale. Also I would like to have my email included tessa@rovingkneadery-example.com
On the backside of my business card I would like to have a appointment reminder on the back side of my business card
listing a space to record client's name, date, time, of appointment.
Also, I made a car magnet at Press Loom with my logo but I would like to change the width of Roving Kneadery and the sentence When worries stack on worries, you knead to set aside a pause to be the width of the logo space. It's hard to read it on the magnet from a distance. I would also like to include my email address tessa@rovingkneadery-example.com

If it is to hard to fit all of that information in the space maybe I could have the logo as two separate downloads. One with the logo picture, the name of the business, Roving Kneadery and the sentence When worries stack on worries, you knead to set aside a pause. The other download just listing my business name, my phone number, my email address, and services offered. Thanks- Henrietta:)

Reason: Hi Bogdan, I have extended the deadline by 7 days so that you do not feel rushed to get the business card project done by Wednesday. The changes that I need done are: 1. Please enlarge the sentence to be the width of the business card. The Roving Kneadery does not to be the width of the business card just the sentence. 2. The curve on the business card if you can change that curve to sky blue and not black. 3. Change the words phone, email, web address, to just icons of a phone, envelope, and the web symbol. 4. Also put my phone, email, web address on the back of my business card. Thanks, Henrietta

```html
<!DOCTYPE html>
<html lang="en">
<head>
<meta charset="utf-8">
<title>Roving Kneadery – Business Card</title>
<link rel="stylesheet" href="https://fonts.googleapis.com/css2?family=Fira+Sans:wght@400;600&family=Alegreya:ital@1&display=swap">
<style>
  :root {
    --orange: #f7931e;
    --orange-soft: #fbc08a;
    --ink: #000000;
    --white: #ffffff;
    --sans: "Fira Sans", sans-serif;
    --serif: "Alegreya", serif;
  }
  html, body {
    margin: 0;
    width: 1200px;
    height: 318px;
    overflow: hidden;
    background: var(--white);
  }
  .canvas {
    position: relative;
    width: 1200px;
    height: 318px;
    font-family: var(--sans);
  }

  /* Front of card */
  .card-front {
    position: absolute;
    left: 0;
    top: 0;
    width: 555px;
    height: 318px;
    background: var(--orange);
    overflow: hidden;
  }
  .front-name {
    position: absolute;
    left: 5px;
    top: -6px;
    margin: 0;
    font-weight: 600;
    font-size: 56px;
    line-height: 66px;
    letter-spacing: 1px;
    color: var(--orange-soft);
    text-transform: uppercase;
    white-space: nowrap;
  }
  .front-artwork {
    position: absolute;
    left: 95px;
    top: 30px;
    width: 370px;
    height: 260px;
  }

  /* Back of card */
  .card-back {
    position: absolute;
    left: 645px;
    top: 0;
    width: 555px;
    height: 318px;
    background: var(--white);
  }
  .back-band {
    position: absolute;
    left: 0;
    top: 2px;
    width: 555px;
    height: 78px;
    background: var(--orange);
  }
  .back-name {
    position: absolute;
    left: 0;
    top: 30px;
    width: 555px;
    margin: 0;
    text-align: center;
    font-weight: 600;
    font-size: 50px;
    line-height: 56px;
    color: var(--white);
    text-transform: uppercase;
    letter-spacing: 0.5px;
    white-space: nowrap;
  }
  .tagline {
    position: absolute;
    left: 19px;
    top: 84px;
    width: 517px;
    margin: 0;
    text-align: center;
    font-family: var(--serif);
    font-style: italic;
    font-size: 19.5px;
    line-height: 24px;
    color: var(--orange);
    white-space: nowrap;
  }
  .appointment-title {
    position: absolute;
    left: 0;
    top: 140px;
    width: 555px;
    margin: 0;
    text-align: center;
    font-size: 19px;
    font-weight: 400;
    line-height: 24px;
    color: var(--orange);
    text-transform: uppercase;
  }
  .field {
    position: absolute;
    top: 196px;
    width: 139px;
    border-top: 1.5px solid var(--orange);
    padding-top: 2px;
    font-family: var(--serif);
    font-style: italic;
    font-size: 12px;
    color: var(--orange);
  }
  .field-name { left: 19px; text-align: left; }
  .field-date { left: 208px; text-align: center; }
  .field-time { left: 397px; text-align: right; }

  .contacts {
    position: absolute;
    left: 19px;
    width: 517px;
    display: flex;
    justify-content: space-between;
    align-items: center;
  }
  .contacts-main { top: 248px; }
  .contacts-web { top: 282px; justify-content: center; }
  .contact {
    display: flex;
    align-items: center;
    gap: 7px;
    margin: 0;
    font-size: 17px;
    line-height: 22px;
    color: var(--orange);
    white-space: nowrap;
  }
  .contact-icon {
    width: 18px;
    height: 18px;
    flex: none;
  }
</style>
</head>
<body>
<main class="canvas">
  <section class="card-front" aria-label="Card front">
    <p class="front-name">Roving Kneadery</p>
    <svg class="front-artwork" viewBox="0 0 370 260" role="img" aria-label="Illustrated mascot artwork with ornamented antlers">
      <rect x="0" y="0" width="370" height="260" rx="60" fill="var(--ink)"/>
    </svg>
  </section>

  <section class="card-back" aria-label="Card back">
    <div class="back-band"></div>
    <h1 class="back-name">Roving Kneadery</h1>
    <p class="tagline">When worries stack on worries, you knead to set aside a pause.</p>
    <h2 class="appointment-title">Appointment</h2>
    <div class="field field-name">name</div>
    <div class="field field-date">date</div>
    <div class="field field-time">time</div>

    <div class="contacts contacts-main">
      <p class="contact contact-email">
        <svg class="contact-icon" viewBox="0 0 18 18" aria-hidden="true">
          <rect x="1.5" y="4" width="15" height="10.5" rx="1.5" fill="none" stroke="var(--orange)" stroke-width="1.6"/>
          <path d="M2 5 L9 10.5 L16 5" fill="none" stroke="var(--orange)" stroke-width="1.6" stroke-linejoin="round"/>
        </svg>
        tessa@rovingkneadery-example.com
      </p>
      <p class="contact contact-phone">
        <svg class="contact-icon" viewBox="0 0 18 18" aria-hidden="true">
          <path d="M4.5 1.8 L7 1.8 L8.2 5.6 L6.3 7 C7.2 9 9 10.8 11 11.7 L12.4 9.8 L16.2 11 L16.2 13.5 C16.2 15 15 16.2 13.5 16.2 C7.4 15.8 2.2 10.6 1.8 4.5 C1.8 3 3 1.8 4.5 1.8 Z" fill="var(--orange)"/>
        </svg>
        555-210-4839
      </p>
    </div>
    <div class="contacts contacts-web">
      <p class="contact contact-web">
        <svg class="contact-icon" viewBox="0 0 18 18" aria-hidden="true">
          <g fill="none" stroke="var(--orange)" stroke-width="1.4">
            <circle cx="9" cy="9" r="7.3"/>
            <ellipse cx="9" cy="9" rx="3.2" ry="7.3"/>
            <line x1="1.7" y1="9" x2="16.3" y2="9"/>
            <path d="M3 5 H15 M3 13 H15"/>
          </g>
        </svg>
        rovingkneadery-example.com
      </p>
    </div>
  </section>
</main>
</body>
</html>
```